Design Home Page Elements

Looking for a concept and 9 images for a box-type home page that displays 8 products and a 'request demo' call to action. Task includes refining the page layout and design of 9 images (logo + 8 products). See attached file for mock-up.
The logo and images shown in the mock-up show all the elements I am looking for - but I would like them rendered in a cleaner, more minimalist style (more like Vorla).
For starters, please just present your rendition of the logo and a single product and I will let you know if you are on the right track. Please feel free to use a different color scheme.
Target Market(s)
B2B. Target market for this product will be technology aware businesses.
Industry/Entity Type
Call

```html
<!DOCTYPE html>
<html lang="en">
<head>
<meta charset="utf-8">
<title>Cirrovox — White Label Communications Platform</title>
<link rel="stylesheet" href="https://fonts.googleapis.com/css2?family=Arimo:wght@400;700&family=Nunito:wght@800&family=Open+Sans:wght@400;600&display=swap">
<style>
  :root{
    --brand-blue:#005b8c;
    --deep-blue:#0b5e8e;
    --ink:#1f1f1f;
    --orange:#e8902a;
    --footer:#2f2f2f;
    --white:#ffffff;
    --divider:rgba(0,0,0,0.10);
  }
  *{box-sizing:border-box;margin:0;padding:0}
  html,body{width:938px;height:1200px;overflow:hidden}
  body{position:relative;background:var(--brand-blue);font-family:"Arimo",Arial,sans-serif;color:var(--white)}

  .site-header{position:absolute;left:0;top:0;width:938px;height:78px;
    background:linear-gradient(#fdfdfd,#eeeeee);border-top:3px solid var(--brand-blue)}
  .site-header::after{content:"";position:absolute;left:386px;top:-1px;border:4px solid transparent;border-top-color:var(--brand-blue)}
  .brand{position:absolute;left:167px;top:24px;font-family:"Nunito",sans-serif;font-weight:800;font-size:30px;color:var(--deep-blue);letter-spacing:-0.3px}
  .main-nav span{position:absolute;top:37px;font-size:12.5px;color:var(--ink)}
  .main-nav .active{color:var(--deep-blue)}
  .search{position:absolute;left:644px;top:37px;width:128px;height:19px;border:1px solid #c8c8c8;border-radius:10px;background:#f4f4f4;
    font-family:"Open Sans",sans-serif;font-size:7.5px;color:#777;padding:4px 9px}
  .search svg{position:absolute;right:6px;top:4px}

  .hero-title{position:absolute;left:0;top:112px;width:938px;text-align:center;font-family:"Nunito",sans-serif;font-weight:800;font-size:24px;letter-spacing:-0.2px}
  .divider{position:absolute;width:1px;background:var(--divider)}

  .product{position:absolute;width:164px;text-align:center}
  .product svg.badge{display:block;margin:0 auto;width:116px;height:118px}
  .product h3{font-size:12.5px;font-weight:700;margin-top:8px;line-height:16px}
  .product p{font-size:10.5px;line-height:13px;margin-top:2px}

  .site-footer{position:absolute;left:0;top:874px;width:938px;height:284px;background:var(--footer)}
  .footer-col{position:absolute;top:58px}
  .footer-col h4{font-size:13.5px;font-weight:700;height:26px;border-bottom:2px solid var(--white);width:116px;position:relative}
  .footer-col h4::after{content:"";position:absolute;left:12px;top:26px;border:4px solid transparent;border-top-color:var(--white)}
  .links{list-style:none;margin-top:8px;font-family:"Open Sans",sans-serif;font-weight:600;font-size:8.5px}
  .links li{height:20px;padding-left:8px;position:relative}
  .links li::before{content:"";position:absolute;left:0;top:3px;border:2.5px solid transparent;border-left:3px solid var(--white)}
  .social{list-style:none;margin-top:8px;font-family:"Open Sans",sans-serif;font-size:12px}
  .social li{display:flex;align-items:center;height:32px;margin-left:-4px}
  .social .dot{width:25px;height:25px;border-radius:50%;margin-right:8px}
  .contact-form{margin-top:8px;width:168px;font-family:"Open Sans",sans-serif;font-size:8px;color:#777}
  .field{background:var(--white);height:20px;padding:4px 8px;margin-bottom:3px;border:1px solid #ddd}
  .field.message{height:51px}
  .submit{width:84px;height:27px;background:var(--brand-blue);color:var(--white);font-family:"Arimo",sans-serif;font-weight:700;font-size:13px;text-align:center;line-height:27px;margin-top:6px}
  .copyright{position:absolute;left:0;top:1158px;width:938px;height:42px;text-align:center;line-height:42px;font-family:"Open Sans",sans-serif;font-size:8.5px}
</style>
</head>
<body>
<svg width="0" height="0" style="position:absolute">
  <defs>
    <radialGradient id="badgeFill" cx="45%" cy="38%" r="65%">
      <stop offset="0" stop-color="#ffffff"/><stop offset=".6" stop-color="#e6ebf0"/><stop offset="1" stop-color="#b9c6d2"/>
    </radialGradient>
    <radialGradient id="demoFill" cx="60%" cy="70%" r="70%">
      <stop offset="0" stop-color="#ffbd6a"/><stop offset=".6" stop-color="#e8902a"/><stop offset="1" stop-color="#b96a10"/>
    </radialGradient>
    <path id="badgeShape" d="M60 8C75 0 95 5 100 20C115 25 120 45 112 60C120 75 115 95 100 100C95 115 75 120 60 112C45 120 25 115 20 100C5 95 0 75 8 60C0 45 5 25 20 20C25 5 45 0 60 8Z"/>
  </defs>
</svg>

<header class="site-header">
  <div class="brand">Cirrovox</div>
  <nav class="main-nav">
    <span class="active" style="left:375px">About</span>
    <span style="left:422px">Services</span>
    <span style="left:483px">Support</span>
    <span style="left:541px">Contact</span>
    <span style="left:597px">Blog</span>
  </nav>
  <div class="search">Enter keyword
    <svg width="10" height="10" viewBox="0 0 10 10"><circle cx="4" cy="4" r="3" fill="none" stroke="#666" stroke-width="1.4"/><line x1="6.2" y1="6.2" x2="9" y2="9" stroke="#666" stroke-width="1.6"/></svg>
  </div>
</header>

<h1 class="hero-title">The Ultimate White Label Communications Plateform</h1>

<div class="divider" style="left:305px;top:160px;height:208px"></div>
<div class="divider" style="left:470px;top:160px;height:208px"></div>
<div class="divider" style="left:634px;top:160px;height:208px"></div>
<div class="divider" style="left:305px;top:386px;height:206px"></div>
<div class="divider" style="left:470px;top:386px;height:206px"></div>
<div class="divider" style="left:634px;top:386px;height:206px"></div>
<div class="divider" style="left:305px;top:610px;height:206px"></div>

<div class="product" style="left:141px;top:178px">
  <svg class="badge" viewBox="0 0 120 120" role="img" aria-label="Hosted PBX product icon"><use href="#badgeShape" fill="url(#badgeFill)" stroke="#0a3f5f" stroke-width="1.5"/></svg>
  <h3>Hosted PBX</h3><p>Lorem ipsum dolor sit<br>amet consectetur</p>
</div>
<div class="product" style="left:305px;top:178px">
  <svg class="badge" viewBox="0 0 120 120" role="img" aria-label="Web conferencing product icon"><use href="#badgeShape" fill="url(#badgeFill)" stroke="#0a3f5f" stroke-width="1.5"/></svg>
  <h3>Web Confrencing</h3><p>Lorem ipsum dolor sit<br>amet consectetur</p>
</div>
<div class="product" style="left:469px;top:178px">
  <svg class="badge" viewBox="0 0 120 120" role="img" aria-label="Instant messaging product icon"><use href="#badgeShape" fill="url(#badgeFill)" stroke="#0a3f5f" stroke-width="1.5"/></svg>
  <h3>Instant Messaging</h3><p>Lorem ipsum dolor sit<br>amet consectetur</p>
</div>
<div class="product" style="left:633px;top:178px">
  <svg class="badge" viewBox="0 0 120 120" role="img" aria-label="Mobile apps product icon"><use href="#badgeShape" fill="url(#badgeFill)" stroke="#0a3f5f" stroke-width="1.5"/></svg>
  <h3>Mobile Apps</h3><p>Lorem ipsum dolor sit<br>amet consectetur</p>
</div>

<div class="product" style="left:141px;top:404px">
  <svg class="badge" viewBox="0 0 120 120" role="img" aria-label="Mobile apps product icon"><use href="#badgeShape" fill="url(#badgeFill)" stroke="#0a3f5f" stroke-width="1.5"/></svg>
  <h3>Mobile Apps</h3><p>Lorem ipsum dolor sit<br>amet consectetur</p>
</div>
<div class="product" style="left:305px;top:404px">
  <svg class="badge" viewBox="0 0 120 120" role="img" aria-label="Customer onboarding product icon"><use href="#badgeShape" fill="url(#badgeFill)" stroke="#0a3f5f" stroke-width="1.5"/></svg>
  <h3>Customer OnBoarding</h3><p>Lorem ipsum dolor sit<br>amet consectetur</p>
</div>
<div class="product" style="left:469px;top:404px">
  <svg class="badge" viewBox="0 0 120 120" role="img" aria-label="Billing and CRM product icon"><use href="#badgeShape" fill="url(#badgeFill)" stroke="#0a3f5f" stroke-width="1.5"/></svg>
  <h3>Billing and CRM</h3><p>Lorem ipsum dolor sit<br>amet consectetur</p>
</div>
<div class="product" style="left:633px;top:404px">
  <svg class="badge" viewBox="0 0 120 120" role="img" aria-label="DID management product icon"><use href="#badgeShape" fill="url(#badgeFill)" stroke="#0a3f5f" stroke-width="1.5"/></svg>
  <h3>DID Management</h3><p>Lorem ipsum dolor sit<br>amet consectetur</p>
</div>

<div class="product" style="left:141px;top:627px">
  <svg class="badge" viewBox="0 0 120 120" role="img" aria-label="Least cost routing product icon"><use href="#badgeShape" fill="url(#badgeFill)" stroke="#0a3f5f" stroke-width="1.5"/></svg>
  <h3>LCR</h3><p>Lorem ipsum dolor sit<br>amet consectetur</p>
</div>
<div class="product" style="left:305px;top:627px">
  <svg class="badge" viewBox="0 0 120 120">
    <use href="#badgeShape" fill="url(#demoFill)" stroke="#5a3300" stroke-width="1.5"/>
    <text x="60" y="67" text-anchor="middle" font-family="Arimo,sans-serif" font-weight="700" font-size="19" fill="#fff">DEMO</text>
  </svg>
  <h3>Request a Demo</h3><p>Lorem ipsum dolor sit<br>amet consectetur</p>
</div>

<footer class="site-footer">
  <div class="footer-col" style="left:167px">
    <h4>Navigation</h4>
    <ul class="links"><li>About</li><li>Services</li><li>Support</li><li>Blog</li></ul>
  </div>
  <div class="footer-col" style="left:314px">
    <h4>Resources</h4>
    <ul class="links"><li>FAQ</li><li>Videos</li><li>Data Sheets</li><li>Screenshots</li></ul>
  </div>
  <div class="footer-col" style="left:460px">
    <h4>Follow us on</h4>
    <ul class="social">
      <li><span class="dot" style="background:#1a74b0"></span>Linkora</li>
      <li><span class="dot" style="background:#2b4a8c"></span>Facenet</li>
      <li><span class="dot" style="background:#2aa5df"></span>Chirper</li>
    </ul>
  </div>
  <div class="footer-col" style="left:602px">
    <h4 style="width:168px">Contact Us</h4>
    <div class="contact-form">
      <div class="field">Your email</div>
      <div class="field">Your Name</div>
      <div class="field message">Your Message</div>
      <div class="submit">Submit</div>
    </div>
  </div>
</footer>
<div class="copyright">Copyright © 2013 Cirrovox</div>
</body>
</html>
```